Business Card for a Life Coaching Company

BRAVOPEAK is a Life Coaching company that was initiated to support people who want to transform thier life or ana aspect of it.
our slogan is : "Dream. Believe. Succeed"
our logo is uploaded.
The name of the company implies that leadership, strength and wisdom required to change your life.
We want an attractive business card that would give an impression of reliability, support and change. so we really want it unique. Here are some examples of unique cards:

http://www.cardcraftvault.example/2009/05/100-really-creative-business-cards/

BravoPeak is a life coaching organization focusing on individual transformation through the application of relevant and timeless principles of success.  BravoPeak believes that real, sustainable life transformations are brought about by tuning into the timeless wisdom we each carry in our hearts while boldy acting in the direction of our dreams.

Contacts on the card:
Address: 7 Tarek Nour El Dine Heliopolis Cairo Egypt
Tel: +202 24 71 38 52
Fax: +202 24 71 38 17
Mobile: +2 012 684 2097 (Dalia Soliman)
+2 0199915815 (Tariq Bhatti)

By the way, our temporary website is http://www.bravopeak.example

We have attached an .eps file with various configurations of our logo.

```html
<!DOCTYPE html>
<html lang="en">
<head>
<meta charset="utf-8">
<title>BravoPeak Business Card</title>
<link rel="stylesheet" href="https://fonts.googleapis.com/css2?family=Cinzel:wght@400;500;600&display=swap">
<style>
  :root {
    --backdrop: #ececec;
    --card: #ffffff;
    --accent: #f26a21;
    --ink: #3a3a3a;
    --logo-grey: #8d8d8d;
    --band-text: #ffffff;
  }
  * { margin: 0; padding: 0; box-sizing: border-box; }
  html, body {
    width: 1200px;
    height: 1004px;
    overflow: hidden;
    background: var(--backdrop);
  }
  .business-card {
    position: absolute;
    left: 75px;
    top: 212px;
    width: 1042px;
    height: 602px;
    background: var(--card);
    font-family: "Cinzel", serif;
    color: var(--ink);
    box-shadow: 3px 4px 10px rgba(0, 0, 0, 0.18);
  }
  .brand {
    position: absolute;
    left: 55px;
    top: 40px;
    display: flex;
    align-items: flex-start;
  }
  .brand-mark {
    width: 96px;
    height: 96px;
    background: var(--accent);
    margin-top: 52px;
  }
  .brand-name {
    margin-left: 32px;
    font-size: 92px;
    font-weight: 400;
    line-height: 100px;
    letter-spacing: -1px;
    color: var(--logo-grey);
  }
  .holder {
    position: absolute;
    right: 38px;
    top: 46px;
    text-align: right;
  }
  .holder-name {
    font-size: 36px;
    font-weight: 500;
    color: var(--accent);
    line-height: 44px;
  }
  .holder-title {
    font-size: 27px;
    font-weight: 500;
    color: var(--ink);
    line-height: 36px;
    letter-spacing: 1px;
  }
  .contact {
    position: absolute;
    left: 62px;
    top: 334px;
    font-size: 24px;
    line-height: 35px;
  }
  .contact-row { display: flex; }
  .contact-label {
    width: 128px;
    color: var(--accent);
  }
  .contact-value { color: var(--ink); }
  .slogan-band {
    position: absolute;
    left: 0;
    bottom: 0;
    width: 100%;
    height: 48px;
    background: var(--accent);
    color: var(--band-text);
    font-size: 24px;
    font-weight: 600;
    letter-spacing: 1px;
    text-align: center;
    line-height: 48px;
  }
</style>
</head>
<body>
  <div class="business-card">
    <div class="brand">
      <div class="brand-mark"></div>
      <div class="brand-name">BRAVO<br>PEAK</div>
    </div>

    <div class="holder">
      <div class="holder-name">Dalia Soliman</div>
      <div class="holder-title">Director</div>
    </div>

    <div class="contact">
      <div class="contact-row"><span class="contact-value">7 Tarek Nour El Dine Heliopolis Cairo Egypt</span></div>
      <div class="contact-row"><span class="contact-label">Web:</span><span class="contact-value">http://www.bravopeak.example</span></div>
      <div class="contact-row"><span class="contact-label">Tel:</span><span class="contact-value">+202 24 71 38 52</span></div>
      <div class="contact-row"><span class="contact-label">Fax:</span><span class="contact-value">+202 24 71 38 17</span></div>
      <div class="contact-row"><span class="contact-label">Mobile:</span><span class="contact-value">+2 012 684 2097</span></div>
    </div>

    <div class="slogan-band">MEANINGFUL LIFE BREAKTHROUGHS...</div>
  </div>
</body>
</html>
```